redesign our website for a law firm

We have a website, need redesign for new web-host-vexly. We need ability to link to tramfund so that we can accept online credit card payment; also need multi-language pages, English, Chinese Polish Russian and Spanish. Need private member log-in function, and blog/news feed ability to make it dynamic, allowing us to publish news/notices. On our site, have Live Chat function, and promote Brisk Vela Online Consultation (fee applies $200/half hour)

Target Market(s)

Immigration Law firm, target individual and corporate clients

Industry/Entity Type

Law Firm

Coding

Coded - Design and coding required

Number of Pages Required

5+ page

Font styles to use
Sans Serif

Colors
f78f20
ffffff
85acd3
3377b5

Requirements
Must have
• multi-language. We have English, Chinese, Polish, Russian and Spanish for the same contents; Online Zoom Consultation (fee applies) Request/Scheduling function
Nice to have
• need link for Tramfund online payment; private password login for clients, and blog/news feeding page, making the site dynamic

```html
<!DOCTYPE html>
<html lang="en">
<head>
<meta charset="utf-8">
<title>KRV Law Group, PLLC</title>
<link href="https://fonts.googleapis.com/css2?family=Lato:ital,wght@0,400;0,700;0,900;1,400&display=swap" rel="stylesheet">
<style>
:root{
  --navy:#0f4a86;
  --blue:#3377b5;
  --sky:#85acd3;
  --orange:#f78f20;
  --cta:#f46a0c;
  --ink:#2b2b2b;
  --text:#444;
  --light:#f4f5f7;
  --white:#fff;
}
*{box-sizing:border-box;margin:0;padding:0}
html,body{width:1200px;height:3600px;overflow:hidden}
body{font-family:'Lato',sans-serif;color:var(--text);background:var(--white);position:relative}
.abs{position:absolute}
.topbar{top:0;left:0;width:1200px;height:56px;background:var(--white)}
.topbar .contact{top:17px;font-size:16px;color:var(--ink)}
.topbar .phone{left:75px;font-weight:700;font-size:18px}
.topbar .mail{left:255px}
.consult{left:646px;top:11px;width:230px;height:35px;background:var(--cta);color:var(--white);font-size:13px;font-weight:700;display:flex;align-items:center;justify-content:center;border-radius:3px}
.login{left:891px;top:11px;width:145px;height:35px;border:1px solid var(--blue);color:var(--blue);font-size:14px;font-weight:700;display:flex;align-items:center;justify-content:center}
.lang{left:1058px;top:19px;font-size:14px;font-weight:700;color:var(--ink)}
.lang::before{content:"";display:inline-block;width:15px;height:10px;background:var(--blue);margin-right:8px;vertical-align:middle}
.header{top:56px;left:0;width:1200px;height:104px;background:var(--light)}
.brand{display:flex;align-items:center;gap:10px;font-weight:700;color:var(--navy);white-space:nowrap}
.brand .dot{width:14px;height:14px;background:var(--navy)}
.nav{top:94px;left:325px;display:flex;font-size:14px;font-weight:700;color:var(--ink)}
.nav span{padding:8px 19px}
.nav .active{background:var(--navy);color:var(--white);border-radius:3px}
.hero{top:160px;left:0;width:1200px;height:620px;background:linear-gradient(110deg,#4a4a4a,#8d8d8d 45%,#5c5c5c)}
.hero h1{position:absolute;top:160px;width:1200px;text-align:center;color:var(--white);font-weight:900;font-size:56px;line-height:58px}
.hero p{position:absolute;top:280px;width:1200px;text-align:center;color:var(--white);font-size:32px;font-weight:700}
.btn{background:var(--cta);color:var(--white);font-weight:700;font-size:19px;border-radius:28px;display:flex;align-items:center;justify-content:center}
.hero .btn{position:absolute;left:503px;top:353px;width:195px;height:55px}
.hero svg{position:absolute;left:0;bottom:0}
.about-bg{top:780px;left:0;width:1200px;height:558px;background:var(--light)}
.photo{border-radius:24px}
h2{font-size:32px;font-weight:900;color:var(--navy);text-transform:uppercase}
.rule{width:70px;height:3px;background:var(--cta)}
.body{font-size:14px;line-height:27.5px;color:var(--text)}
.section-title{width:1200px;text-align:center;left:0}
.card-img{width:240px;height:192px;clip-path:polygon(8% 0,100% 0,92% 100%,0 100%);border-radius:14px}
.pa-title{font-size:21px;font-weight:700;color:var(--ink);line-height:25px}
.att-bg{top:1842px;left:0;width:1200px;height:566px;background:var(--light)}
.att{width:240px;text-align:center}
.att .img{width:240px;height:194px;clip-path:polygon(8% 0,100% 0,92% 100%,0 100%)}
.att .name{margin-top:42px;font-size:19px;color:var(--ink)}
.att .role{font-size:16px;color:var(--blue);font-style:italic;margin-top:6px}
.att .soc{margin-top:18px;display:flex;justify-content:center;gap:18px}
.soc i{display:block;width:16px;height:16px;border-radius:50%;background:#a3a3a3}
.arrow{font-size:30px;color:#555;font-weight:700}
.news-card{width:332px;height:275px;background:var(--light);border-radius:12px;padding:26px 24px}
.news-card .date{font-size:17px;font-weight:900;color:var(--navy)}
.news-card h3{font-size:21px;font-weight:700;color:var(--ink);line-height:28px;margin-top:12px}
.news-card p{font-size:14.5px;line-height:26px;margin-top:12px}
.news-card .more{font-size:14px;font-weight:900;color:var(--cta);margin-top:14px}
.loc-bg{top:2912px;left:0;width:1200px;height:408px;background:var(--light)}
.loc h4{font-size:21px;font-weight:700;color:var(--ink);line-height:25px}
.loc .firm{font-size:15px;font-weight:900;color:var(--navy);margin-top:16px}
.loc p{font-size:14.5px;line-height:28.5px;margin-top:4px}
.foot h5{font-size:15px;font-weight:900;color:#333;text-transform:uppercase}
.foot .col{font-size:14.5px;line-height:35px;margin-top:6px}
.pay{font-size:14px;font-weight:700;color:var(--navy);display:flex;align-items:center;gap:8px}
.pay::before{content:"";width:12px;height:12px;background:var(--navy)}
</style>
</head>
<body>

<div class="abs topbar">
  <div class="abs contact phone">&#9990; 555-201-4410</div>
  <div class="abs contact mail">&#9993; info@krvlawgroup.example</div>
  <div class="abs consult">BOOK BRISK VELA CONSULTATION</div>
  <div class="abs login">PRIVATE LOG IN</div>
  <div class="abs lang">EN &#8964;</div>
</div>

<header class="abs header"></header>
<div class="abs brand" style="left:75px;top:94px;font-size:20px"><span class="dot"></span>KRV Law Group, PLLC</div>
<nav class="abs nav">
  <span class="active">HOME</span><span>ABOUT US</span><span>PRACTICE AREAS</span><span>ATTORNEYS</span><span>RESOURCES</span><span>FAQ</span><span>CONTACT US</span>
</nav>

<section class="abs hero" role="img" aria-label="Attorneys meeting with a client in a law office">
  <h1>WELCOME TO<br>KRV LAW GROUP</h1>
  <p>We are a New York based international law firm.</p>
  <div class="btn">READ MORE</div>
  <svg width="1200" height="50" viewBox="0 0 1200 50"><path d="M0 20 Q300 50 600 38 T1200 16 V50 H0Z" fill="var(--light)"/><path d="M0 20 Q300 50 600 38 T1200 16 V28 Q900 38 600 48 Q300 56 0 36Z" fill="var(--navy)"/></svg>
</section>

<div class="abs about-bg"></div>
<div class="abs photo" style="left:75px;top:855px;width:512px;height:407px;background:linear-gradient(135deg,#c9a27a,#8a6a4e 60%,#e9d8c4)" role="img" aria-label="Legal team seated around a conference table"></div>
<h2 class="abs" style="left:615px;top:846px">About Us</h2>
<div class="abs rule" style="left:615px;top:893px"></div>
<div class="abs body" style="left:615px;top:913px;width:510px">
  <p>KRV Law Group, PLLC (“KRV”), is a New York based international law firm with a practice focused upon the complex arena of United States Immigration Law, and Commercial and Civil Litigation. Established on the highest principles of integrity, ethics and an earnest passion for excellence, KRV attorneys provide first class legal counsel for companies, families and individuals, both inside the United States and globally around the world.</p>
  <p style="margin-top:10px">As experienced immigration attorneys, we primarily concentrate upon Business Immigration matters by assisting clients in obtaining temporary work visas.</p>
</div>
<div class="abs btn" style="left:615px;top:1207px;width:195px;height:55px">READ MORE</div>

<h2 class="abs" style="left:75px;top:1380px">Practice Areas</h2>
<div class="abs rule" style="left:75px;top:1427px"></div>
<div class="abs arrow" style="left:810px;top:1378px">&#8249; &#8250;</div>
<div class="abs body" style="left:75px;top:1448px;width:760px;line-height:25px">Founded by Ms. Mira T. Delacourt in early 1999, KRV provides first class legal counsel for companies, families and individuals locally, nationally and globally, with particular expertise in:</div>
<div class="abs card-img" style="left:75px;top:1524px;background:linear-gradient(135deg,#d9d9d9,#7a7a7a)" role="img" aria-label="Hands filling out an immigration form"></div>
<div class="abs card-img" style="left:345px;top:1524px;background:linear-gradient(135deg,#cfcfcf,#5e5e5e)" role="img" aria-label="Signing a business contract"></div>
<div class="abs card-img" style="left:615px;top:1524px;background:linear-gradient(135deg,#bdbdbd,#4d4d4d)" role="img" aria-label="Litigation team in discussion"></div>
<div class="abs pa-title" style="left:73px;top:1738px">Immigration<br>Law</div>
<div class="abs pa-title" style="left:344px;top:1738px">Business &amp;<br>Contract Law</div>
<div class="abs pa-title" style="left:614px;top:1738px">Commercial &amp;<br>Civil Litigation</div>
<div class="abs" style="left:884px;top:1338px;width:316px;height:504px;clip-path:polygon(12% 0,100% 0,100% 100%,0 100%,0 95%);border-bottom-left-radius:30px;background:linear-gradient(160deg,#e6e0d6,#a3846a 55%,#6e5a48)" role="img" aria-label="Professional in a team meeting"></div>

<div class="abs att-bg"></div>
<h2 class="abs section-title" style="top:1896px">Our Attorneys</h2>
<div class="abs arrow" style="left:47px;top:2168px">&#8249;</div>
<div class="abs arrow" style="left:1138px;top:2168px">&#8250;</div>
<div class="abs att" style="left:75px;top:1996px"><div class="img" style="background:linear-gradient(135deg,#d8d2cb,#8c7a6a)" role="img" aria-label="Portrait of Mira T. Delacourt"></div><div class="name">Mira T. Delacourt</div><div class="role">Principal Attorney</div><div class="soc"><i></i><i></i><i></i></div></div>
<div class="abs att" style="left:345px;top:1996px"><div class="img" style="background:linear-gradient(135deg,#6a6560,#2e2a27)" role="img" aria-label="Portrait of Owen R. Falk"></div><div class="name">Owen R. Falk</div><div class="role">Of Counsel</div><div class="soc"><i></i><i></i><i></i></div></div>
<div class="abs att" style="left:615px;top:1996px"><div class="img" style="background:linear-gradient(135deg,#d7e2ec,#8fa3b6)" role="img" aria-label="Portrait of Peter J. Lindqvist"></div><div class="name">Peter J. Lindqvist</div><div class="role">Of Counsel</div><div class="soc"><i></i><i></i><i></i></div></div>
<div class="abs att" style="left:885px;top:1996px"><div class="img" style="background:linear-gradient(135deg,#9a8c7e,#4f463f)" role="img" aria-label="Portrait of Daniel Reyes"></div><div class="name">Daniel Reyes</div><div class="role">Of Counsel</div><div class="soc"><i></i><i></i><i></i></div></div>

<div class="abs" style="left:0;top:2408px;width:405px;height:504px;clip-path:polygon(0 0,86% 0,100% 100%,0 100%);border-bottom-right-radius:30px;background:linear-gradient(150deg,#d9c8b4,#a0714b 55%,#5a4a3c)" role="img" aria-label="Lawyer consulting with a client at a desk"></div>
<h2 class="abs" style="left:433px;top:2472px">Latest News</h2>
<div class="abs rule" style="left:433px;top:2519px"></div>
<div class="abs arrow" style="left:1082px;top:2470px">&#8249; &#8250;</div>
<article class="abs news-card" style="left:433px;top:2558px"><div class="date">SEP10, 2020</div><h3>Neque porro quisquam est qui dolorem ipsum quia</h3><p>Proin felis nulla, pulvinar egestas metus eu, gravida iaculis velit. Sed eget arcu at massa mattis aliquet. Integer et sapien id mi tempus auctor.</p><div class="more">READ MORE</div></article>
<article class="abs news-card" style="left:795px;top:2558px"><div class="date">SEP10, 2020</div><h3>Neque porro quisquam est qui dolorem ipsum quia</h3><p>Proin felis nulla, pulvinar egestas metus eu, gravida iaculis velit. Sed eget arcu at massa mattis aliquet. Integer et sapien id mi tempus auctor.</p><div class="more">READ MORE</div></article>

<div class="abs loc-bg"></div>
<h2 class="abs section-title" style="top:2962px">Our Locations</h2>
<div class="abs loc" style="left:75px;top:3056px;width:290px"><h4>LIC, New York Office:</h4><div class="firm">KRV Law Group, PLLC</div><p>27-40 Harbor Row, Suite 400 LIC,<br>NY 11190<br>Phone No.: 555-201-4410<br>Fax No.: 555-201-4411<br>E-mail: info@krvlawgroup.example</p></div>
<div class="abs loc" style="left:441px;top:3056px;width:320px"><h4>Manhattan, New York Office:</h4><div class="firm">KRV Law Group, PLLC</div><p>318 Larkspur Avenue, Suite 1803 New York,<br>NY 10090<br>Phone No.: 555-318-2270<br>E-mail: info@krvlawgroup.example</p></div>
<div class="abs loc" style="left:828px;top:3056px;width:300px"><h4>Long Island, Nassau County,<br>New York:</h4><div class="firm">KRV Law Group, PLLC</div><p>9 Meadow Lane, Ste. 303 Elm Cove,<br>NY 11590<br>Phone No.: 555-640-3385<br>Fax No.: 555-640-3386<br>E-mail: info@krvlawgroup.example</p></div>

<footer>
<div class="abs brand" style="left:75px;top:3400px;font-size:19px"><span class="dot"></span>KRV Law Group, PLLC</div>
<div class="abs" style="left:75px;top:3492px;font-size:12.5px;line-height:20px;color:#333">Copyright © 2020. Company Name<br>All Rights Reserved. Disclaimer</div>
<div class="abs soc" style="left:75px;top:3552px;display:flex;gap:20px"><i></i><i></i><i></i><i></i><i></i></div>
<div class="abs foot" style="left:350px;top:3374px"><h5>Site Map</h5>
  <div class="col" style="display:grid;grid-template-columns:133px 120px">
  <span>Home</span><span>Resources</span><span>About Us</span><span>FAQ</span><span>Practice Areas</span><span>Contact Us</span><span>Attorneys</span></div></div>
<div class="abs foot" style="left:626px;top:3374px"><h5>Practice Areas</h5>
  <div class="col">Immigration Law<br>Business and Contract Law<br>Commercial and Civil litigation<br>Corporate Finance and Security Law</div></div>
<div class="abs foot" style="left:932px;top:3374px"><h5>Office Hours</h5>
  <div class="col" style="line-height:27px;margin-top:10px">Mondays through Fridays,<br>10:30a.m. to 6:30p.m.<br>Eastern Standard Time.</div>
  <div class="pay" style="margin-top:20px">Tramfund</div></div>
</footer>

</body>
</html>
```